Plant your Garden - Landing Page Visual

Looking to polish up this visual. This will be a landing page for a career progression site that employees use to see what is required to promote from one position to another. We want to stick to a Nautical theme. Each of the icons will be used to hyperlink to another page. The design needs to use our Colors as you see in the Tolvin logo attachment. The RGB color for the orange is 255,67,16. The design needs to use a nautical compass and have a swooping upward ribbon or arrow effect. The files need to be given is AI format as each of the icons need to be transferred as a separate Vector file as well.

```html
<!DOCTYPE html>
<html lang="en">
<head>
<meta charset="utf-8">
<title>Tolvin – Plant your Garden</title>
<link rel="stylesheet" href="https://fonts.googleapis.com/css2?family=Montserrat:wght@500;600;800&display=swap">
<style>
  :root {
    --orange: rgb(255, 67, 16);
    --arrow-orange: #f7931e;
    --arrow-soft: #fbc27a;
    --ink: #111111;
    --paper: #ffffff;
    --sky-deep: #3f8bd3;
    --sky-mid: #8fc0ea;
    --sky-pale: #dcecf8;
    --compass-light: #ffffff;
    --compass-shade: #d9d9d9;
  }
  * { margin: 0; padding: 0; box-sizing: border-box; }
  html, body {
    width: 1200px;
    height: 937px;
    overflow: hidden;
    background: var(--paper);
    font-family: "Montserrat", Arial, sans-serif;
  }
  .landing {
    position: absolute;
    left: 96px;
    top: 111px;
    width: 1008px;
    height: 713px;
    overflow: hidden;
    background: var(--paper);
  }
  .sky {
    position: absolute;
    inset: 0;
    background: linear-gradient(180deg, var(--sky-deep) 0%, var(--sky-mid) 35%, var(--sky-pale) 62%, var(--paper) 82%);
  }
  .growth-arrow {
    position: absolute;
    inset: 0;
    background: linear-gradient(200deg, var(--arrow-orange) 0%, var(--arrow-soft) 100%);
    clip-path: polygon(560px 713px, 880px 600px, 900px 420px, 1008px 400px, 1008px 713px);
  }
  .brand {
    position: absolute;
    left: 87px;
    top: 24px;
    display: flex;
    align-items: center;
    gap: 10px;
  }
  .brand-mark {
    width: 30px;
    height: 30px;
    background: var(--ink);
  }
  .brand-name {
    font-size: 40px;
    font-weight: 500;
    letter-spacing: 1px;
    color: var(--ink);
    line-height: 1;
    text-transform: uppercase;
  }
  .menu-toggle {
    position: absolute;
    left: 907px;
    top: 28px;
    width: 33px;
    display: flex;
    flex-direction: column;
    gap: 5px;
  }
  .menu-toggle span {
    display: block;
    height: 2px;
    background: var(--ink);
  }
  .artwork {
    position: absolute;
    inset: 0;
  }
  .career-label {
    position: absolute;
    left: 777px;
    font-size: 18px;
    font-weight: 500;
    line-height: 23px;
    color: var(--ink);
  }
  .headline {
    position: absolute;
    left: 97px;
    top: 582px;
    text-transform: uppercase;
    line-height: 1;
  }
  .headline-lead {
    display: block;
    font-size: 30px;
    font-weight: 600;
    color: var(--ink);
  }
  .headline-main {
    display: block;
    margin-top: 6px;
    font-size: 76px;
    font-weight: 800;
    color: var(--orange);
    letter-spacing: 1px;
  }
</style>
</head>
<body>
<main class="landing">
  <div class="sky" role="img" aria-label="Blue sky with scattered white clouds fading to white"></div>

  <div class="growth-arrow" role="img" aria-label="Large orange arrow sweeping upward to the right"></div>

  <svg class="artwork" width="1008" height="713" viewBox="0 0 1008 713">
    <defs>
      <radialGradient id="compass-fill" cx="50%" cy="50%" r="50%">
        <stop offset="0%" stop-color="var(--compass-light)"/>
        <stop offset="80%" stop-color="var(--compass-light)"/>
        <stop offset="100%" stop-color="var(--compass-shade)"/>
      </radialGradient>
    </defs>

    <g class="course-ribbons">
      <path fill="var(--orange)" d="M450 318 C560 318 600 108 700 108 L700 196 C600 196 560 342 450 342 Z"/>
      <path fill="var(--ink)" d="M450 344 C560 344 600 205 700 205 L700 293 C600 293 560 368 450 368 Z"/>
      <path fill="var(--orange)" d="M450 372 C560 372 600 312 700 312 L700 400 C600 400 560 396 450 396 Z"/>
      <path fill="var(--ink)" d="M450 400 C560 400 600 412 700 412 L700 500 C600 500 560 426 450 426 Z"/>
      <path fill="var(--orange)" d="M450 430 C560 430 600 515 700 515 L700 603 C600 603 560 456 450 456 Z"/>
    </g>

    <circle class="compass" cx="297" cy="353" r="190" fill="url(#compass-fill)" role="img" aria-label="Nautical compass rose with black and orange points"/>

    <g class="career-icons" stroke-width="6">
      <g class="career-link">
        <circle cx="704" cy="152" r="45" fill="var(--paper)" stroke="var(--orange)"/>
        <rect x="682" y="132" width="22" height="16" fill="var(--ink)" stroke="none"/>
        <rect x="690" y="148" width="6" height="12" fill="var(--ink)" stroke="none"/>
        <rect x="682" y="160" width="22" height="14" fill="var(--ink)" stroke="none"/>
        <circle cx="716" cy="138" r="7" fill="var(--ink)" stroke="none"/>
        <rect x="707" y="148" width="18" height="26" rx="4" fill="var(--ink)" stroke="none"/>
      </g>
      <g class="career-link">
        <circle cx="704" cy="249" r="45" fill="var(--paper)" stroke="var(--ink)"/>
        <rect x="678" y="234" width="32" height="24" fill="var(--ink)" stroke="none"/>
        <path d="M712 240 H722 L730 250 V258 H712 Z" fill="var(--ink)" stroke="none"/>
        <circle cx="688" cy="261" r="5" fill="var(--ink)" stroke="var(--paper)" stroke-width="2"/>
        <circle cx="720" cy="261" r="5" fill="var(--ink)" stroke="var(--paper)" stroke-width="2"/>
      </g>
      <g class="career-link">
        <circle cx="704" cy="356" r="45" fill="var(--paper)" stroke="var(--orange)"/>
        <rect x="680" y="338" width="4" height="32" fill="var(--ink)" stroke="none"/>
        <rect x="684" y="364" width="14" height="3" fill="var(--ink)" stroke="none"/>
        <rect x="684" y="346" width="12" height="12" fill="var(--ink)" stroke="none"/>
        <path d="M700 348 H716 L722 360 H728 V370 H700 Z" fill="var(--ink)" stroke="none"/>
        <circle cx="706" cy="373" r="5" fill="var(--ink)" stroke="var(--paper)" stroke-width="2"/>
        <circle cx="722" cy="373" r="5" fill="var(--ink)" stroke="var(--paper)" stroke-width="2"/>
      </g>
      <g class="career-link">
        <circle cx="704" cy="456" r="45" fill="var(--paper)" stroke="var(--ink)"/>
        <rect x="696" y="430" width="30" height="20" fill="none" stroke="var(--ink)" stroke-width="3"/>
        <circle cx="686" cy="436" r="5" fill="var(--ink)" stroke="none"/>
        <rect x="681" y="443" width="10" height="13" rx="2" fill="var(--ink)" stroke="none"/>
        <circle cx="688" cy="466" r="4" fill="var(--ink)" stroke="none"/>
        <circle cx="704" cy="466" r="4" fill="var(--ink)" stroke="none"/>
        <circle cx="720" cy="466" r="4" fill="var(--ink)" stroke="none"/>
        <rect x="682" y="472" width="12" height="8" rx="2" fill="var(--ink)" stroke="none"/>
        <rect x="698" y="472" width="12" height="8" rx="2" fill="var(--ink)" stroke="none"/>
        <rect x="714" y="472" width="12" height="8" rx="2" fill="var(--ink)" stroke="none"/>
      </g>
      <g class="career-link">
        <circle cx="704" cy="559" r="45" fill="var(--paper)" stroke="var(--orange)"/>
        <circle cx="704" cy="559" r="20" fill="none" stroke="var(--ink)" stroke-width="6"/>
        <circle cx="704" cy="561" r="6" fill="var(--ink)" stroke="none"/>
        <path d="M686 556 Q704 550 722 556" fill="none" stroke="var(--ink)" stroke-width="5"/>
        <rect x="701" y="563" width="6" height="15" fill="var(--ink)" stroke="none"/>
      </g>
    </g>
  </svg>

  <div class="brand">
    <span class="brand-mark"></span>
    <span class="brand-name">Tolvin</span>
  </div>

  <nav class="menu-toggle" aria-label="Menu"><span></span><span></span><span></span></nav>

  <p class="career-label" style="top:129px">Equipment<br>Operator</p>
  <p class="career-label" style="top:226px">Delivery<br>Driver</p>
  <p class="career-label" style="top:333px">Werehouse<br>Specialist</p>
  <p class="career-label" style="top:433px">Trainning<br>Specialist</p>
  <p class="career-label" style="top:536px">Spec Lead<br>Delivery</p>

  <h1 class="headline">
    <span class="headline-lead">Plant your</span>
    <span class="headline-main">Garden</span>
  </h1>
</main>
</body>
</html>
```